Real Estate Graphics and Ad Redesign - Digital Marketing Assets

I am looking for someone to create a variety of custom graphics for our company and redesign some of our existing ads and digital marketing material. Please see attached. Look for redesign of graphics and chart to look good and clear and clean.

Target Market(s)

Real Estate Lead generation, mortgage lenders and Business 2 Business Sales

Industry/Entity Type

Real Estate

Font styles to use
Serif
Sans Serif

Colors
f78f20
33a6d7
0a91cc
fac994
fff5ef
cee9f5
b868aa
add136
e667a6

Requirements
Must have
• Must be clean, easy to understand, friendly and custom look and feel. I like the concept of future and tech but at the same time elegant and well thought out. The idea is that the concepts we are explaining and what we are doing is somewhat complex and thus clarity and appeal are required.
Nice to have
• Custom graphics and visual representations of texts
Should not have
• Complicated or hard to digest layout. Overly busy and hard colors, it should be sleek, easy to digest.

```html
<!DOCTYPE html>
<html lang="en">
<head>
<meta charset="utf-8">
<title>Keyward – Marketing Cards</title>
<link href="https://fonts.googleapis.com/css2?family=Montserrat:wght@300;400;500;800&family=Oswald:wght@300&display=swap" rel="stylesheet">
<style>
  :root{
    --orange:#f78f20;
    --blue:#0a91cc;
    --sky:#33a6d7;
    --peach:#fac994;
    --cream:#fbfaf5;
    --ice:#cee9f5;
    --lilac:#a9a6de;
    --ink:#3a3a3a;
    --body:#4a4a4a;
    --page:#ebebeb;
  }
  *{margin:0;padding:0;box-sizing:border-box}
  html,body{width:1200px;height:2227px;overflow:hidden;background:var(--page)}
  body{position:relative;font-family:"Montserrat",Arial,sans-serif;color:var(--body)}
  .card{position:absolute;left:50px;width:1100px;height:620px;background:var(--cream);overflow:hidden;box-shadow:0 6px 18px rgba(0,0,0,.18)}
  .card--value{top:428px;border-bottom:10px solid var(--orange)}
  .card--tms{top:1178px}
  .corner-wave{position:absolute;left:0;top:0}
  .brand{position:absolute;left:45px;top:60px;width:340px;height:92px;background:#fff;display:flex;align-items:center;justify-content:center;gap:12px}
  .brand--tms{left:72px;top:26px;width:310px;height:98px}
  .brand__mark{width:22px;height:22px;background:var(--orange)}
  .brand__name{font-weight:800;font-size:34px;letter-spacing:2px;color:var(--orange)}
  .headline{position:absolute;left:93px;top:188px;line-height:1.12;font-weight:normal}
  .headline--tms{left:102px;top:140px}
  .headline__accent{display:block;font-weight:800;font-size:40px;color:var(--orange);letter-spacing:1px}
  .headline__plain{display:block;font-weight:300;font-size:40px;color:var(--ink);letter-spacing:1px}
  .headline__bar{width:108px;height:5px;background:var(--blue);margin-top:12px}
  .points{position:absolute;left:93px;top:318px;list-style:none}
  .point{display:flex;align-items:center;gap:14px;margin-bottom:14px}
  .point--abs{position:absolute;left:98px;margin:0}
  .point__num{font-family:"Oswald",sans-serif;font-weight:300;font-size:34px;color:var(--sky);width:30px;line-height:1;flex:none}
  .point__text{font-size:13px;line-height:1.25;max-width:380px}
  .point__text--wide{max-width:520px}
  .site{position:absolute;left:90px;top:536px;font-size:12px;letter-spacing:3px;color:var(--ink)}
  .site-line{position:absolute;left:390px;top:543px;width:570px;height:1px;background:#c9c9c9}
  .art{position:absolute}
  .art--value{left:560px;top:80px;width:540px;height:430px;background:radial-gradient(ellipse at 55% 45%,#2f9ea3 0%,#5cc0c4 35%,var(--ice) 60%,rgba(251,250,245,0) 75%),linear-gradient(180deg,rgba(0,0,0,0) 60%,var(--orange) 62%,var(--orange) 80%,rgba(0,0,0,0) 82%);border-radius:40% 20% 30% 40%}
  .art--tms{left:730px;top:30px;width:370px;height:590px;background:linear-gradient(160deg,var(--ice) 0%,#b7c7ea 45%,var(--lilac) 100%);border-radius:45% 0 0 30%}
  .ticks{position:absolute;top:365px;display:grid;gap:14px}
  .ticks--left{left:112px;width:275px}
  .ticks--right{left:415px;width:285px;gap:20px}
  .tick{display:flex;gap:10px;font-size:12.5px;line-height:1.2}
  .tick svg{flex:none;margin-top:2px}
</style>
</head>
<body>

<section class="card card--value">
  <svg class="corner-wave" width="200" height="90" viewBox="0 0 200 90"><path d="M0 0H200C160 8 130 20 110 40C85 62 40 50 0 85Z" fill="var(--blue)"/></svg>
  <div class="brand"><span class="brand__mark"></span><span class="brand__name">KEYWARD</span></div>
  <h1 class="headline">
    <span class="headline__accent">REAL VALUE AND</span>
    <span class="headline__plain">REAL PARTNERSHIPS</span>
    <span class="headline__bar" style="display:block"></span>
  </h1>
  <ol class="points">
    <li class="point"><span class="point__num">01</span><span class="point__text">Keyward maintains the relationship with buyers and agents via an exclusive 2 year agreement</span></li>
    <li class="point"><span class="point__num">02</span><span class="point__text">Keyward manages the home search process for all parties; which enables consistent communication</span></li>
    <li class="point"><span class="point__num">03</span><span class="point__text">Keyward uses preferred title companies for a smoother transaction</span></li>
    <li class="point"><span class="point__num">04</span><span class="point__text">Keyward engages with all parties post closing and continues the relationship</span></li>
  </ol>
  <div class="site">www.keyward-example.com</div>
  <div class="site-line"></div>
  <div class="art art--value" role="img" aria-label="Illustration of two partners shaking hands on sofas beside stacks of coins, with floating chart, idea and media icons"></div>
</section>

<section class="card card--tms">
  <svg class="corner-wave" width="190" height="90" viewBox="0 0 190 90"><path d="M0 0H190C150 8 125 22 105 40C80 62 40 50 0 82Z" fill="var(--orange)"/></svg>
  <div class="brand brand--tms"><span class="brand__mark"></span><span class="brand__name">KEYWARD</span></div>
  <h1 class="headline headline--tms">
    <span class="headline__accent">TRANSACTION</span>
    <span class="headline__accent">MANAGEMENT SYSTEM</span>
    <span class="headline__plain">&amp; SUPPORT TEAM</span>
    <span class="headline__bar" style="display:block"></span>
  </h1>
  <div class="point point--abs" style="top:312px"><span class="point__num">01</span><span class="point__text point__text--wide">Keyward manages all pre-qualified buyers via our Keyward Link -Transaction Management System - from pre-approval issue to close</span></div>
  <div class="ticks ticks--left">
    <div class="tick"><svg width="16" height="16" viewBox="0 0 16 16"><circle cx="8" cy="8" r="6.5" fill="none" stroke="var(--orange)" stroke-width="1.5"/><path d="M5 8l2.2 2.2L13 4" fill="none" stroke="var(--orange)" stroke-width="1.6"/></svg><span>Keyward Link is currently creating a 20% faster time to get a buyer to contract with a 55% higher conversion rate to close with our Lending Partner. 90% of buyers close with the original lender assigned through both lead channels</span></div>
    <div class="tick"><svg width="16" height="16" viewBox="0 0 16 16"><circle cx="8" cy="8" r="6.5" fill="none" stroke="var(--orange)" stroke-width="1.5"/><path d="M5 8l2.2 2.2L13 4" fill="none" stroke="var(--orange)" stroke-width="1.6"/></svg><span>Keyward Link will produce bi-weekly buyer updates to assigned LO or branch</span></div>
  </div>
  <div class="ticks ticks--right">
    <div class="tick"><svg width="16" height="16" viewBox="0 0 16 16"><circle cx="8" cy="8" r="6.5" fill="none" stroke="var(--orange)" stroke-width="1.5"/><path d="M5 8l2.2 2.2L13 4" fill="none" stroke="var(--orange)" stroke-width="1.6"/></svg><span>Specific buying stage and substage insight/reporting available to LO</span></div>
    <div class="tick"><svg width="16" height="16" viewBox="0 0 16 16"><circle cx="8" cy="8" r="6.5" fill="none" stroke="var(--orange)" stroke-width="1.5"/><path d="M5 8l2.2 2.2L13 4" fill="none" stroke="var(--orange)" stroke-width="1.6"/></svg><span>Dedicated Keyward Prime team will manage all aspects of the transaction - phone calls, e-mails, SMS, scheduling and partner Real Estate Agent relationship</span></div>
  </div>
  <div class="point point--abs" style="top:540px"><span class="point__num">02</span><span class="point__text point__text--wide">Keyward has the ability to offset the Lending Partner's advertising spend through purchasing of pre-qualified buyer leads or lead acquisition</span></div>
  <div class="art art--tms" role="img" aria-label="Illustration of people with a large coin, card and shopping cart above a laptop showing the transaction pipeline dashboard"></div>
</section>

</body>
</html>
```